CareLumen business cards

We need a business card design that we could customize as needed for employees. We will need space for Name, Title, 1-2 phone numbers and email address.

We are a Pharmacy Benefits Management (PBM) company for hospice agencies and beginning a nationwide expansion. Attached is a vector file of our logo.

Cards can be single or double sided.

```html
<!DOCTYPE html>
<html lang="en">
<head>
<meta charset="utf-8">
<title>CareLumen business cards</title>
<link rel="stylesheet" href="https://fonts.googleapis.com/css2?family=Questrial&display=swap">
<style>
  :root {
    --backdrop: #2b2b2b;
    --card: #f4f4f2;
    --card-edge: #e6e6e3;
    --brand-green: #8a9a4a;
    --brand-blue: #3a78a8;
    --ink: #2e2e2e;
    --ink-soft: #4a4a4a;
    --rule: #4f7ea6;
  }
  * { margin: 0; padding: 0; box-sizing: border-box; }
  html, body {
    width: 1200px; height: 900px; overflow: hidden;
    background: var(--backdrop);
    font-family: "Questrial", "Century Gothic", sans-serif;
  }
  .canvas { position: relative; width: 1200px; height: 900px; }
  .card {
    position: absolute; left: 354px; width: 488px; height: 271px;
    background: var(--card);
    border-radius: 30px 4px 30px 4px;
    border: 1px solid var(--card-edge);
    overflow: hidden;
  }
  .card--front { top: 157px; }
  .card--back { top: 466px; }
  .brand { position: absolute; display: flex; align-items: center; }
  .brand__square {
    display: block; border-radius: 6px; background: var(--brand-blue);
  }
  .brand__name { color: var(--brand-green); line-height: 1; letter-spacing: -0.5px; }
  .card--front .brand { left: 36px; top: 101px; gap: 14px; }
  .card--front .brand__square { width: 66px; height: 66px; }
  .card--front .brand__name { font-size: 54px; }
  .card--back .brand { left: 25px; top: 36px; gap: 12px; }
  .card--back .brand__square { width: 60px; height: 60px; }
  .card--back .brand__name { font-size: 50px; }
  .holder {
    position: absolute; left: 23px; top: 170px;
    font-size: 20px; color: var(--ink);
  }
  .holder__title {
    font-size: 12.5px; letter-spacing: 0.4px; text-transform: uppercase;
    margin-left: 4px; color: var(--ink-soft);
  }
  .contacts {
    position: absolute; left: 23px; top: 225px;
    display: flex; font-size: 13px; color: var(--ink-soft);
  }
  .contacts__item { position: relative; padding-right: 6px; white-space: nowrap; }
  .contacts__item + .contacts__item { padding-left: 6px; }
  .contacts__item + .contacts__item::before {
    content: ""; position: absolute; left: 0; top: -2px; width: 1px; height: 48px;
    background: var(--rule);
  }
  .contacts__label { color: var(--rule); margin-right: 3px; }
</style>
</head>
<body>
<main class="canvas">
  <section class="card card--front" aria-label="Card front">
    <div class="brand">
      <span class="brand__square" aria-hidden="true"></span>
      <span class="brand__name">CareLumen</span>
    </div>
  </section>

  <section class="card card--back" aria-label="Card back">
    <div class="brand">
      <span class="brand__square" aria-hidden="true"></span>
      <span class="brand__name">CareLumen</span>
    </div>
    <p class="holder">Dana Whitfield <span class="holder__title">Operation Manager</span></p>
    <p class="contacts">
      <span class="contacts__item"><span class="contacts__label">T</span>(221) 33 410 22 18</span>
      <span class="contacts__item"><span class="contacts__label">M</span>(221) 77 504 61 33</span>
      <span class="contacts__item"><span class="contacts__label">E</span>dana@carelumen.com</span>
    </p>
  </section>
</main>
</body>
</html>
```